hi all

Im after a new age looking business card with my company logo on it

must include these details, I would like the PH and Email to be symbols

If the colours used for card could be kept within the colours used in logo that I have supplied that would be great, if another colour is to be used dark grey would be ok. no light bulbs etc thanks

Details below to be incorporated on card

Damian Holloway

Lic E871302

PH 0219647381

E info@brightvaleelectrical.example.nz

Domestic Commercial Industrial Electricians

```html
<!DOCTYPE html>
<html lang="en">
<head>
<meta charset="utf-8">
<title>Brightvale Electrical – Business Card</title>
<link href="https://fonts.googleapis.com/css2?family=Arimo&family=Montserrat:wght@300;700&display=swap" rel="stylesheet">
<style>
  :root {
    --frame: #b8d8ec;
    --card-front: #0e1215;
    --card-back: #101114;
    --brand-blue: #1479c2;
    --white: #ffffff;
  }
  html, body {
    margin: 0;
    width: 1200px;
    height: 1200px;
    overflow: hidden;
    background: var(--frame);
  }
  .card {
    position: absolute;
    left: 12px;
    width: 1176px;
    overflow: hidden;
  }
  .card-front {
    top: 11px;
    height: 585px;
    background: var(--card-front);
  }
  .card-back {
    top: 601px;
    height: 585px;
    background: var(--card-back);
  }
  .brand-mark {
    position: absolute;
    left: 50%;
    top: 196px;
    width: 118px;
    height: 118px;
    margin-left: -59px;
    border: 7px solid var(--brand-blue);
    border-radius: 50%;
    box-sizing: border-box;
  }
  .brand-name {
    position: absolute;
    left: 0;
    right: 0;
    top: 326px;
    margin: 0;
    text-align: center;
    font-family: "Montserrat", sans-serif;
    font-weight: 700;
    font-size: 44px;
    letter-spacing: 3px;
    text-transform: uppercase;
    color: var(--brand-blue);
  }
  .tagline {
    position: absolute;
    left: 0;
    right: 0;
    top: 516px;
    margin: 0;
    text-align: center;
    font-family: "Arimo", sans-serif;
    font-size: 29px;
    color: var(--white);
  }
  .holder-name {
    position: absolute;
    left: 115px;
    top: 96px;
    margin: 0;
    font-family: "Montserrat", sans-serif;
    font-weight: 700;
    font-size: 41px;
    letter-spacing: 2.5px;
    text-transform: uppercase;
    color: var(--brand-blue);
  }
  .licence {
    position: absolute;
    left: 115px;
    top: 143px;
    margin: 0;
    font-family: "Arimo", sans-serif;
    font-size: 35px;
    color: var(--brand-blue);
  }
  .contact {
    position: absolute;
    left: 115px;
    display: flex;
    align-items: center;
    font-family: "Montserrat", sans-serif;
    font-weight: 300;
    font-size: 33px;
    color: var(--brand-blue);
  }
  .contact svg { flex: none; fill: var(--brand-blue); }
  .contact-phone { top: 362px; }
  .contact-phone svg { width: 48px; height: 50px; margin-right: 22px; }
  .contact-email { top: 445px; }
  .contact-email svg { width: 52px; height: 36px; margin-right: 18px; }
</style>
</head>
<body>
  <section class="card card-front">
    <div class="brand-mark"></div>
    <h1 class="brand-name">Brightvale Electrical</h1>
    <p class="tagline">Domestic Commercial Industrial Electricians</p>
  </section>

  <section class="card card-back">
    <h2 class="holder-name">Damian Holloway</h2>
    <p class="licence">Lic E871302</p>

    <div class="contact contact-phone">
      <svg viewBox="0 0 48 50" aria-hidden="true">
        <path d="M11 1c3-2 5-1 6 1l3 7c1 2 0 4-2 5l-3 2c2 5 7 11 12 14l2-2c2-2 4-2 6-1l6 3c2 1 3 3 1 6l-2 2c-3 3-7 4-11 2C17 36 6 26 2 14 1 9 2 6 5 4z"/>
      </svg>
      <span>0219647381</span>
    </div>

    <div class="contact contact-email">
      <svg viewBox="0 0 52 36" aria-hidden="true">
        <path d="M2 0h48L26 20z"/>
        <path d="M0 3l18 15L0 34z"/>
        <path d="M52 3L34 18l18 16z"/>
        <path d="M20 20l6 5 6-5 17 16H3z"/>
      </svg>
      <span>info@brightvaleelectrical.example.nz</span>
    </div>
  </section>
</body>
</html>
```